Bref créative
KORVO FREIGHT
BUSINESS CARDS AND BROCHURE LAYOUT
Professional
Reed Quandt
Owner/Specialist
I want no address
korvofreight@nubramail.com
www.korvofreight-example.com
just the logo on the back

```html
<!DOCTYPE html>
<html lang="en">
<head>
<meta charset="utf-8">
<title>Korvo Freight Stationery</title>
<link href="https://fonts.googleapis.com/css2?family=Arimo:wght@400;700&display=swap" rel="stylesheet">
<style>
:root{
  --red:#c8102e;
  --red-dark:#8e0c20;
  --grey:#9a9a9a;
  --grey-light:#d9d9d9;
  --ink:#333;
  --black:#111;
  --paper:#fff;
}
*{box-sizing:border-box;margin:0;padding:0}
html,body{width:1200px;height:538px;overflow:hidden;background:var(--paper)}
body{position:relative;font-family:Arimo,Arial,sans-serif;color:var(--ink)}
.sheet{position:absolute;background:var(--paper);box-shadow:0 1px 4px rgba(0,0,0,.35);overflow:hidden}
.swoosh{position:absolute;left:0;width:100%;display:block}
.swoosh.bottom{bottom:0}
.swoosh.top{top:0}
.brand{font-weight:700;color:var(--red);white-space:nowrap;display:flex;align-items:center;gap:3px;letter-spacing:.3px}
.brand .dot{width:6px;height:6px;border-radius:50%;background:var(--red);flex:none}
.brand.white{color:var(--paper)}
.brand.white .dot{background:var(--paper)}
.copy{font-size:5.5px;line-height:1.45;color:var(--ink)}
.copy.light{color:var(--paper)}
.photo{position:absolute;background:linear-gradient(160deg,#e9eef2,#b9c1c7 55%,#6f7a80)}
.panel{position:absolute;top:0;height:100%}
.heading{font-size:9px;font-weight:700;color:var(--paper);letter-spacing:.4px}
/* cards */
.card{position:absolute;top:19px;width:103px;height:48px;border-radius:2px;box-shadow:0 1px 3px rgba(0,0,0,.35);overflow:hidden;display:flex;align-items:center;justify-content:center}
.card .brand{font-size:7.5px}
.card-black{background:var(--black)}
.card-red{background:var(--red)}
.card-white{background:var(--paper)}
.card-details{position:absolute;right:6px;top:6px;text-align:right;font-size:4.2px;line-height:1.4}
/* form */
.form-table{position:absolute;left:26px;top:82px;width:178px;border-collapse:collapse}
.form-table td{border:.6px solid #888;height:11px;font-size:5px;padding:0 3px}
.form-table td.label{width:30px;font-weight:700}
.checks{position:absolute;left:26px;top:160px;display:flex;gap:10px;font-size:5px}
.checks span::before{content:"";display:inline-block;width:5px;height:5px;border:.6px solid #666;margin-right:2px;vertical-align:-1px}
.envelope{position:absolute;left:893px;width:295px;box-shadow:0 1px 4px rgba(0,0,0,.35);overflow:hidden;background:var(--paper)}
</style>
</head>
<body>

<!-- Brochure outside -->
<section class="sheet brochure-outside" style="left:0;top:5px;width:372px;height:235px">
  <div class="panel" style="left:0;width:120px;background:var(--red)">
    <div class="photo" style="left:0;top:0;width:120px;height:92px" role="img" aria-label="Photo of a white delivery van"></div>
    <div style="position:absolute;left:8px;top:102px;right:8px">
      <div class="heading">OUR COMPANY</div>
      <p class="copy light" style="margin-top:6px">Fast regional freight with care, on time and fully tracked from pickup to door.</p>
      <p class="copy light" style="margin-top:5px">Trusted by local shops.</p>
    </div>
  </div>
  <div class="panel" style="left:120px;width:125px;border-right:.5px solid var(--grey-light)">
    <div style="position:absolute;left:10px;top:24px;right:10px">
      <p class="copy">We move parcels and pallets across the region every day.</p>
      <p class="copy" style="margin-top:8px">Ask about weekly routes.</p>
      <p class="copy" style="margin-top:8px">Same day service available.</p>
    </div>
    <svg class="swoosh bottom" viewBox="0 0 125 40" preserveAspectRatio="none" height="40"><path d="M0 18 C40 34 85 30 125 8 V40 H0Z" fill="var(--grey)"/><path d="M0 26 C45 40 90 36 125 18 V40 H0Z" fill="var(--red)"/></svg>
  </div>
  <div class="panel" style="left:245px;width:127px">
    <svg class="swoosh top" viewBox="0 0 127 22" preserveAspectRatio="none" height="22"><path d="M0 0 H127 V6 C80 20 40 18 0 4Z" fill="var(--grey-light)"/></svg>
    <div style="position:absolute;left:0;right:0;top:52px;display:flex;flex-direction:column;align-items:center">
      <div class="brand" style="font-size:11px"><span class="dot"></span>KORVO FREIGHT</div>
      <p class="copy" style="margin-top:4px;color:var(--grey)">Freight you can trust</p>
      <p class="copy" style="margin-top:40px;text-align:center;padding:0 12px">Call us for a free quote.</p>
    </div>
    <svg class="swoosh bottom" viewBox="0 0 127 40" preserveAspectRatio="none" height="40"><path d="M0 10 C40 30 85 32 127 16 V40 H0Z" fill="var(--grey)"/><path d="M0 20 C45 38 90 38 127 26 V40 H0Z" fill="var(--red)"/></svg>
  </div>
</section>

<!-- Brochure inside -->
<section class="sheet brochure-inside" style="left:0;top:270px;width:372px;height:263px">
  <div class="panel" style="left:0;width:120px;background:var(--red)">
    <div style="position:absolute;left:9px;top:16px;right:9px">
      <p class="copy light">Our drivers know every road and every customer by name.</p>
      <p class="copy light" style="margin-top:8px;font-weight:700">Reliable. Fast. Friendly.</p>
    </div>
    <svg class="swoosh bottom" viewBox="0 0 120 40" preserveAspectRatio="none" height="40"><path d="M0 18 C40 34 80 30 120 10 V40 H0Z" fill="var(--red-dark)"/></svg>
  </div>
  <div class="panel" style="left:120px;width:125px;border-right:.5px solid var(--grey-light)">
    <p class="copy" style="position:absolute;left:10px;top:18px;right:10px">Flexible vans for any load size.</p>
    <div class="photo" style="left:8px;top:92px;width:109px;height:72px" role="img" aria-label="Photo of a white van on the road"></div>
  </div>
  <div class="panel" style="left:245px;width:127px">
    <p class="copy" style="position:absolute;left:10px;top:18px;right:10px">Contact us today for rates.</p>
    <svg class="swoosh bottom" viewBox="0 0 127 60" preserveAspectRatio="none" height="60"><path d="M0 20 C45 45 90 40 127 14 V60 H0Z" fill="var(--grey-light)"/><path d="M0 36 C45 55 90 52 127 34 V60 H0Z" fill="var(--grey)"/></svg>
  </div>
</section>

<!-- Business cards -->
<div class="card card-white" style="left:389px">
  <div class="card-details"><b>Reed Quandt</b><br>Owner/Specialist<br>korvofreight@nubramail.com<br>www.korvofreight-example.com</div>
  <div class="brand" style="position:absolute;left:6px;bottom:8px;font-size:6.5px"><span class="dot"></span>KORVO FREIGHT</div>
  <svg class="swoosh bottom" viewBox="0 0 103 8" preserveAspectRatio="none" height="6"><path d="M0 4 C40 8 70 8 103 0 V8 H0Z" fill="var(--red)"/></svg>
</div>
<div class="card card-black" style="left:509px"><div class="brand white"><span class="dot"></span>KORVO FREIGHT</div></div>
<div class="card card-red" style="left:629px"><div class="brand white"><span class="dot"></span>KORVO FREIGHT</div></div>
<div class="card card-white" style="left:749px"><div class="brand"><span class="dot"></span>KORVO FREIGHT</div></div>

<!-- Fax form -->
<section class="sheet form-sheet" style="left:389px;top:91px;width:230px;height:437px">
  <svg class="swoosh top" viewBox="0 0 230 30" preserveAspectRatio="none" height="30"><path d="M110 0 H230 V26 C190 10 150 4 110 0Z" fill="var(--grey-light)"/></svg>
  <div class="brand" style="position:absolute;left:26px;top:24px;font-size:10px"><span class="dot"></span>KORVO FREIGHT</div>
  <table class="form-table">
    <tr><td class="label">Date</td><td></td><td class="label">Pages</td><td></td></tr>
    <tr><td class="label">To</td><td></td><td class="label">Ref</td><td></td></tr>
    <tr><td class="label">From</td><td></td><td class="label"></td><td></td></tr>
    <tr><td class="label"></td><td></td><td class="label"></td><td></td></tr>
  </table>
  <div class="checks"><span>Urgent</span><span>Review</span><span>Reply</span><span>Recycle</span></div>
  <svg class="swoosh bottom" viewBox="0 0 230 60" preserveAspectRatio="none" height="60"><path d="M0 14 C80 50 160 48 230 20 V60 H0Z" fill="var(--grey)"/><path d="M0 30 C80 60 160 58 230 36 V60 H0Z" fill="var(--red)"/></svg>
</section>

<!-- Letterhead -->
<section class="sheet letterhead" style="left:634px;top:91px;width:230px;height:437px">
  <svg class="swoosh top" viewBox="0 0 230 30" preserveAspectRatio="none" height="30"><path d="M110 0 H230 V26 C190 10 150 4 110 0Z" fill="var(--grey-light)"/></svg>
  <div class="brand" style="position:absolute;left:0;right:0;top:28px;justify-content:center;font-size:11px"><span class="dot"></span>KORVO FREIGHT</div>
  <svg class="swoosh bottom" viewBox="0 0 230 60" preserveAspectRatio="none" height="60"><path d="M0 14 C80 50 160 48 230 20 V60 H0Z" fill="var(--grey)"/><path d="M0 30 C80 60 160 58 230 36 V60 H0Z" fill="var(--red)"/></svg>
</section>

<!-- Envelopes -->
<section class="envelope" style="top:72px;height:168px">
  <svg class="swoosh top" viewBox="0 0 295 30" preserveAspectRatio="none" height="30"><path d="M0 0 H295 V8 C200 28 90 26 0 6Z" fill="var(--grey)"/><path d="M0 0 H295 V2 C200 20 90 18 0 0Z" fill="var(--red)"/></svg>
  <div class="brand" style="position:absolute;left:14px;top:36px;font-size:9px"><span class="dot"></span>KORVO FREIGHT</div>
  <svg class="swoosh bottom" viewBox="0 0 295 40" preserveAspectRatio="none" height="40"><path d="M0 14 C100 42 200 40 295 12 V40 H0Z" fill="var(--grey)"/><path d="M0 26 C100 46 200 44 295 24 V40 H0Z" fill="var(--red)"/></svg>
</section>
<section class="envelope" style="top:248px;height:70px;background:var(--red)">
  <svg class="swoosh top" viewBox="0 0 295 40" preserveAspectRatio="none" height="40"><path d="M0 0 H295 L147 40Z" fill="var(--red-dark)"/></svg>
</section>
<section class="envelope" style="top:312px;height:66px">
  <svg class="swoosh top" viewBox="0 0 295 36" preserveAspectRatio="none" height="36"><path d="M0 0 H295 L147 36Z" fill="var(--red)"/></svg>
</section>
<section class="envelope" style="top:386px;height:137px">
  <svg class="swoosh top" viewBox="0 0 295 60" preserveAspectRatio="none" height="60"><path d="M0 0 H295 L147 60Z" fill="var(--grey-light)"/></svg>
  <div class="brand" style="position:absolute;left:0;right:0;top:72px;justify-content:center;font-size:9px"><span class="dot"></span>KORVO FREIGHT</div>
</section>

</body>
</html>
```